Flyer Design & Business Cards

I have tried to make up some flyer and have attached them as info with what we would like included. I would like them made to look more professional and I would like business cards along the same line.

Industry/Entity Type

Business

```html
<!DOCTYPE html>
<html lang="en">
<head>
<meta charset="utf-8">
<title>Saltmarsh Inn – Flyer</title>
<link href="https://fonts.googleapis.com/css2?family=Dosis:wght@500;600&family=Nunito+Sans:wght@400;700;800&display=swap" rel="stylesheet">
<style>
  :root{
    --stage:#e9e9e9;
    --navy:#1f5d8b;
    --navy-deep:#1a5380;
    --gold:#f5a93a;
    --gold-dark:#d98f22;
    --white:#ffffff;
    --head-font:"Dosis", sans-serif;
    --body-font:"Nunito Sans", sans-serif;
  }
  *{box-sizing:border-box;margin:0;padding:0}
  html,body{width:1200px;height:1200px;overflow:hidden;background:var(--stage)}
  .flyer{position:absolute;top:183px;width:568px;height:802px;overflow:hidden;
    background:linear-gradient(180deg,var(--navy) 0%,var(--navy-deep) 100%);color:var(--white);font-family:var(--body-font)}
  .flyer--front{left:24px}
  .flyer--back{left:609px}
  .abs{position:absolute}
  .center{left:0;right:0;text-align:center}
  .corner{position:absolute;width:96px;height:96px;background:rgba(245,169,58,.1);border-radius:6px}
  .corner--tl{left:20px;top:26px}.corner--tr{right:20px;top:26px}
  .corner--bl{left:20px;bottom:26px}.corner--br{right:20px;bottom:26px}
  .photo{position:absolute;border-radius:50%;border:3px solid var(--white);transform:translate(-50%,-50%)}
  .photo--lg{width:116px;height:116px}
  .photo--md{width:112px;height:112px}
  .brand-name{position:absolute;left:0;right:0;text-align:center;color:var(--gold);font-family:var(--body-font);font-weight:800;line-height:1}
  .ribbon{position:absolute;background:var(--gold);color:var(--navy-deep);font-family:var(--head-font);font-weight:600;
    display:flex;align-items:center;justify-content:center;transform:rotate(-3deg);outline:2px solid var(--white);outline-offset:-6px}
  .ribbon-link{position:absolute;background:var(--gold-dark);transform:skewY(8deg)}
  .tagline{font-family:var(--head-font);font-weight:500;font-size:17px;letter-spacing:.3px}
  .headline{font-family:var(--head-font);font-weight:600;font-size:25px}
  .copy{font-size:13.6px;line-height:19px;padding:0 22px}
  .offer{position:absolute;left:53px;width:460px;top:491px;height:52px;border-radius:26px;background:var(--gold);
    color:var(--navy-deep);font-family:var(--body-font);font-weight:700;font-size:13.2px;line-height:17px;
    display:flex;align-items:center;justify-content:center;text-align:center}
  .rule{position:absolute;left:67px;width:448px;height:1.5px;background:var(--gold)}
  .map{position:absolute;left:212px;top:606px;width:144px;height:144px;border-radius:50%;border:3px solid var(--gold);
    background:radial-gradient(circle at 45% 45%,#e6eef2 0%,#bcd9ea 70%,#8fc2e0 100%)}
  .address{position:absolute;left:31px;width:200px;top:640px;text-align:center;font-size:13.6px;line-height:18.6px;font-style:normal}
  .contact{position:absolute;left:350px;width:182px;top:640px;text-align:center;font-size:13.6px;line-height:18.6px}
  .contact strong{font-weight:800}
  .social{margin-top:6px;font-weight:700;font-size:12px}
</style>
</head>
<body>

<section class="flyer flyer--front">
  <div class="corner corner--tl" role="img" aria-label="Scrolled corner ornament"></div>
  <div class="corner corner--tr" role="img" aria-label="Scrolled corner ornament"></div>
  <div class="corner corner--bl" role="img" aria-label="Scrolled corner ornament"></div>
  <div class="corner corner--br" role="img" aria-label="Scrolled corner ornament"></div>

  <div class="photo photo--lg" style="left:160px;top:103px;background:radial-gradient(#c8742c,#4a2616)" role="img" aria-label="Pint of ale at the bar"></div>
  <div class="photo photo--lg" style="left:284px;top:103px;background:radial-gradient(#8a7560,#3a2a20)" role="img" aria-label="Bottle of aged rum on sand"></div>
  <div class="photo photo--lg" style="left:407px;top:103px;background:radial-gradient(#b59d80,#5a4028)" role="img" aria-label="Bottles of spirits on sand"></div>

  <div class="brand-name" style="top:282px;font-size:60px">Saltmarsh</div>
  <div class="brand-name" style="top:350px;font-size:60px">Inn</div>

  <div class="ribbon-link" style="left:214px;top:490px;width:150px;height:26px"></div>
  <div class="ribbon" style="left:176px;top:452px;width:184px;height:48px;font-size:24px">THE ONLY PUB</div>
  <div class="ribbon" style="left:208px;top:508px;width:182px;height:48px;font-size:24px">IN NORTH ISLE</div>

  <p class="abs center tagline" style="top:577px">REAL ALES . BAR FOOD . LIVE MUSIC</p>

  <div class="photo photo--lg" style="left:160px;top:691px;background:radial-gradient(#c23a32,#3b2418)" role="img" aria-label="Red ale pump clip on the bar"></div>
  <div class="photo photo--lg" style="left:284px;top:691px;background:radial-gradient(#9a3f1a,#2b1a12)" role="img" aria-label="Glass of dark ale"></div>
  <div class="photo photo--lg" style="left:407px;top:691px;background:radial-gradient(#b05a4a,#3a2020)" role="img" aria-label="Shelves of bottles behind the bar"></div>
</section>

<section class="flyer flyer--back">
  <div class="corner corner--tl" role="img" aria-label="Scrolled corner ornament"></div>
  <div class="corner corner--tr" role="img" aria-label="Scrolled corner ornament"></div>
  <div class="corner corner--bl" role="img" aria-label="Scrolled corner ornament"></div>
  <div class="corner corner--br" role="img" aria-label="Scrolled corner ornament"></div>

  <div class="brand-name" style="top:96px;font-size:36px">Saltmarsh</div>
  <div class="brand-name" style="top:136px;font-size:36px">Inn</div>

  <h2 class="abs center headline" style="top:200px">THE ONLY PUB IN NORTH ISLE</h2>

  <div class="photo photo--md" style="left:161px;top:304px;background:radial-gradient(#b08058,#4a3020)" role="img" aria-label="Bar room with pool table"></div>
  <div class="photo photo--md" style="left:282px;top:304px;background:radial-gradient(#9a3fb0,#2a1440)" role="img" aria-label="Evening crowd in the bar"></div>
  <div class="photo photo--md" style="left:402px;top:304px;background:linear-gradient(180deg,#8fb6e0 0%,#6a6a6a 55%,#7f9a5a 100%)" role="img" aria-label="Stone inn building exterior"></div>

  <p class="abs center copy" style="top:374px">Saltmarsh Inn is a Georgian listed building located on the west side of<br>North Isle, on the edge of the Atlantic, owned and run by<br>Morag and Ewan Fraser.</p>
  <p class="abs center copy" style="top:439px">“Saltmarsh” is a friendly pub with a traditional Hebridean atmosphere and<br>stocks an extensive range of drinks including real ales from Cairn Brewery.</p>

  <div class="offer">WE OFFER A VARIETY OF HOME-COOKED FOOD INCLUDING<br>LOCAL PRODUCE WHEN AVAILABLE.</div>

  <p class="abs center copy" style="top:555px">Facilities: TV, free Wi-Fi, pool table, darts, table-games and outdoor games.<br>There is outdoor seating for sunny days/evenings.</p>

  <div class="rule" style="top:631px"></div>
  <div class="rule" style="top:722px"></div>
  <div class="map" role="img" aria-label="Map of the island showing the inn location"></div>

  <address class="address">Saltmarsh Inn<br>Shore Road, Baymouth<br>North Isle<br>HS9 4QT</address>
  <div class="contact">
    <strong>01234 567890</strong><br>
    www.saltmarshinn.com
    <p class="social">@saltmarshinn</p>
  </div>
</section>

</body>
</html>
```